Innovative healthcare collaborative needs new look for business cards

CareLoomQ is a new kind of healthcare relationship company focused on aligning partners, innovation and solutions to provide needed health services to healthcare systems, hospitals or private business. Not mired in the old merger and acquisition fee-for-service framework, we focus on primary, secondary and tertiary service area partnership collaboratives. These networks are constructed by aligning healthcare services along a network of care, not just an individual patient care plan. This involves partnership arrangements with large or small medical centers, physician groups, allied health services, public health agencies, health insurers, et al as well as civic agencies, schools, farmers, supply chains to bring about needed healthcare solutions for patients. Think Green Havens. GH does for communities what we do for hospitals and health systems. We educate and instruct on strategic, operational, and innovative solutions for a healthcare provider, practice, business, or system resulting in successful construction of care networks (legal entity). We provide the blueprint of how to do this type of partnership, focused on what’s best for the sustainability of the business and the people (patients or potential patients) living there. Rural hospitals in particular are at risk.
We also provide seminars to academic, medical academic, and private industry to instruct on how to construct these care networks and educate on the essential criteria to be successful in the new healthcare era. We have been doing this work for the past 8 years, and since COVID-19, the recognition of fractured processes has boosted the demand. We need a business card that sets the tone that the traditional healthcare delivery system in the US has transformed (overnight). Our company is educating on how to transition current business models to the new world order in this space.
Brainstormed some business card tag lines for consideration:
CareLoomQ
• a healthcaring company
• allbettertogether
• connecting for the greater good

Target Market(s)

Health systems, hospitals, physician practices, academic medical schools, residency programs

Industry/Entity Type

Healthcare

Contact Information for Business Card

Doreen Vashtoll, Chief Relationship Officer
doreenvashtoll@mailpost-example.net
mobile: 415-286-9043

Font styles to use
Serif
Sans Serif

Requirements
Should not have
• Do not use word Consultant

```html
<!DOCTYPE html>
<html lang="en">
<head>
<meta charset="utf-8">
<title>CareLoomQ Business Cards</title>
<link href="https://fonts.googleapis.com/css2?family=Cabin:wght@400;700&display=swap" rel="stylesheet">
<style>
  :root {
    --backdrop: #262626;
    --navy: #2f4a82;
    --navy-text: #2b4a8c;
    --red: #e23a3a;
    --paper: #f4f4f2;
    --white: #ffffff;
    --ink: #2a3d6e;
  }
  * { margin: 0; padding: 0; box-sizing: border-box; }
  html, body { width: 1200px; height: 922px; overflow: hidden; }
  body {
    background: var(--backdrop);
    font-family: "Cabin", "Gill Sans", sans-serif;
    position: relative;
  }
  .card {
    position: absolute;
    width: 520px;
    height: 296px;
    box-shadow: 0 10px 30px rgba(0,0,0,.45);
  }
  .card-front {
    left: 150px; top: 90px;
    background: var(--navy);
    display: flex; align-items: center; justify-content: center;
  }
  .card-back {
    left: 530px; top: 430px;
    background: var(--paper);
  }

  .wordmark { display: flex; align-items: center; gap: 12px; }
  .wordmark-dot { border-radius: 50%; flex: none; }
  .wordmark-name { font-weight: 400; line-height: 1; letter-spacing: .5px; }

  .card-front .wordmark-dot { width: 26px; height: 26px; background: var(--white); }
  .card-front .wordmark-name { color: var(--white); font-size: 46px; }

  .card-back .wordmark { position: absolute; left: 34px; bottom: 46px; gap: 9px; }
  .card-back .wordmark-dot { width: 16px; height: 16px; background: var(--navy-text); }
  .card-back .wordmark-name { color: var(--navy-text); font-size: 28px; }

  .contact { position: absolute; left: 290px; top: 78px; }
  .contact-name { color: var(--ink); font-size: 21px; font-weight: 400; }
  .contact-name strong { font-weight: 700; }
  .contact-title { color: var(--red); font-size: 11px; letter-spacing: .4px; text-transform: uppercase; margin-top: 2px; }
  .contact-rule { width: 34px; height: 1px; background: var(--red); margin: 14px 0 12px; }
  .contact-line { display: flex; align-items: center; gap: 7px; color: var(--ink); font-size: 11px; margin-bottom: 6px; }
  .contact-line svg { width: 11px; height: 11px; flex: none; }

  .lockup { position: absolute; left: 760px; top: 818px; gap: 14px; }
  .lockup .wordmark-dot { width: 34px; height: 34px; background: var(--navy-text); }
  .lockup .wordmark-name { color: var(--navy-text); font-size: 56px; }
</style>
</head>
<body>
  <section class="card card-front">
    <div class="wordmark">
      <span class="wordmark-dot"></span>
      <div class="wordmark-name">CareLoomQ</div>
    </div>
  </section>

  <section class="card card-back">
    <div class="contact">
      <div class="contact-name">Doreen <strong>Vashtoll</strong></div>
      <div class="contact-title">Chief Relationship Officer</div>
      <div class="contact-rule"></div>
      <div class="contact-line">
        <svg viewBox="0 0 12 12"><rect x="0.5" y="2" width="11" height="8" rx="1" fill="var(--red)"/><path d="M1 2.5 L6 6.5 L11 2.5" stroke="#fff" stroke-width="1" fill="none"/></svg>
        <span>doreenvashtoll@mailpost-example.net</span>
      </div>
      <div class="contact-line">
        <svg viewBox="0 0 12 12"><path d="M3 1 L5 3.5 L4 5 Q5 7.5 7 8 L8.5 7 L11 9 L9.5 11 Q4 10.5 1 3 Z" fill="var(--red)"/></svg>
        <span>415-286-9043</span>
      </div>
    </div>
    <div class="wordmark">
      <span class="wordmark-dot"></span>
      <div class="wordmark-name">CareLoomQ</div>
    </div>
  </section>

  <div class="lockup wordmark">
    <span class="wordmark-dot"></span>
    <div class="wordmark-name">CareLoomQ</div>
  </div>
</body>
</html>
```